Wedding page for Linda and Daniel

we need a webpage for our wedding. The website contains the basic information of the wedding. like general information, timetable, map, contact information and a photo section, more you find in the attached word document.
attached you see our invitation cards, design should have similarties like the cards.
We like green colours and as its a weeding page it can be romantic. :-)
Industry/Entity Type
Wedding
Coding
Coded - Design and coding required
Number of Pages Required
3 page
Font styles to use
Serif
Sans Serif
Decorative
Script
Colors
a5ce39
Requirements
Must have
- a clear structure and a simple navigation as there are 5 to 7 navigation points
- The weeding date should be clearly visible 26.05.2018.
- All labels and translation have to be editable by my (in HTML code or psd code is fine) --> the final page will be in german
Nice to have
- if the webdesign has some similarities with the wedding card.
- if there is a time counter till the wedding is coming.
- a modern way to display the program of the wedding day.
- the domain is kolvarenplitz.ch and would be cool to integrate somehow.
- if the website should be responsive.
Should not have
- no special logo or something needed.

```html
<!DOCTYPE html>
<html lang="en">
<head>
<meta charset="utf-8">
<title>Linda &amp; Daniel – Wedding</title>
<link href="https://fonts.googleapis.com/css2?family=Dancing+Script:wght@600;700&family=Lora:ital,wght@0,400;0,700;1,400&family=Lato:wght@400;700&display=swap" rel="stylesheet">
<style>
:root{
  --green:#8fac4f;
  --green-soft:#a9bf6c;
  --green-pale:#dbe5bd;
  --leaf-deep:#b3cb7c;
  --cream:#f8f4e2;
  --paper:#f3f2ec;
  --pill:#e6e4d9;
  --rope:#7d6a4a;
  --ink:#4c4a45;
  --ink-soft:#77746b;
  --dash:#b9b6aa;
  --white:#ffffff;
}
*{box-sizing:border-box;margin:0;padding:0}
html,body{width:1200px;height:3600px;overflow:hidden}
body{position:relative;background:var(--cream);font-family:"Lora",Georgia,serif;color:var(--ink)}
.foliage{position:absolute;top:0;width:132px;height:3600px;
  background:repeating-linear-gradient(170deg,var(--cream) 0 80px,var(--green-pale) 80px 120px,var(--leaf-deep) 120px 134px,var(--green-pale) 134px 160px,var(--cream) 160px 230px)}
.foliage--left{left:0}
.foliage--right{right:0}
.page{position:absolute;left:132px;top:90px;width:936px;height:3460px;background:var(--paper);box-shadow:0 0 12px rgba(0,0,0,.08)}
.rope{position:absolute;height:5px;background:repeating-linear-gradient(90deg,var(--rope) 0 6px,#a08c65 6px 10px);border-radius:3px}
.masthead{position:absolute;left:396px;top:40px;width:408px;height:150px;background:var(--pill);border-radius:40px;text-align:center}
.masthead__names{font-family:"Dancing Script",cursive;font-weight:600;color:var(--green);font-size:54px;line-height:1;margin-top:22px;word-spacing:4px}
.masthead__date{font-family:"Lora",serif;font-size:29px;color:var(--ink);margin-top:14px}
.countdown{position:absolute;top:235px;left:298px;display:flex;gap:14px}
.countdown__unit{width:140px;height:96px;border:2px dashed var(--dash);text-align:center;color:var(--green)}
.countdown__value{font-size:44px;line-height:1;margin-top:12px}
.countdown__label{font-family:"Lato",sans-serif;font-size:14px;letter-spacing:2px;margin-top:8px}
.hero{position:absolute;left:173px;top:360px;width:854px;height:461px;background:linear-gradient(160deg,#b9a783,#cfbd92 55%,#a69474);box-shadow:0 6px 10px rgba(0,0,0,.15)}
.hero__domain{position:absolute;right:26px;bottom:16px;font-family:"Lora",serif;font-size:34px;color:var(--white);letter-spacing:1px}
.nav{position:absolute;left:132px;top:864px;width:936px;height:44px;background:var(--green-soft);border-top:2px dashed var(--white);border-bottom:2px dashed var(--white);outline:3px solid var(--green-soft);display:flex;justify-content:center;align-items:center;gap:28px;font-family:"Lato",sans-serif;font-size:13px;color:var(--white)}
.nav__dot{width:5px;height:5px;background:var(--white);border-radius:50%}
.section-title{position:absolute;left:132px;width:936px;height:60px}
.section-title::before{content:"";position:absolute;left:0;right:0;top:28px;height:4px;background:var(--rope)}
.section-title span{position:absolute;left:50%;top:0;transform:translateX(-50%);width:300px;height:60px;line-height:60px;background:var(--pill);border-radius:30px;text-align:center;font-family:"Lato",sans-serif;font-size:22px;color:var(--ink)}
.card{position:absolute;border:2px dashed var(--dash);background:var(--paper)}
.portrait{position:absolute;width:170px;height:140px;background:var(--white);padding:8px;box-shadow:0 3px 8px rgba(0,0,0,.2)}
.portrait div{width:100%;height:100%}
.script-title{font-family:"Dancing Script",cursive;font-weight:600;color:var(--green);font-size:36px;line-height:1.1;word-spacing:4px}
.story__title{text-align:center;margin-top:54px;font-size:46px}
.story__text{font-size:13px;line-height:21px;text-align:center;color:var(--ink);padding:0 40px;margin-top:20px}
.sprig{position:absolute;width:110px;height:90px;border-radius:50% 10% 50% 50%;background:radial-gradient(ellipse at 70% 30%,var(--leaf-deep),var(--green-pale) 60%,transparent 72%)}
.venue{padding:38px 30px}
.venue__item{display:flex;align-items:flex-start;gap:16px;font-size:14px;margin-top:22px}
.venue__item svg{flex:none}
.venue__link{display:block;font-style:italic;color:var(--green);margin-top:8px}
.program{position:absolute;left:0}
.program__row{display:flex;align-items:center;height:40px;margin-bottom:22px}
.program__time{width:100px;height:40px;line-height:40px;background:var(--green-soft);color:var(--white);font-family:"Lato",sans-serif;font-size:17px;letter-spacing:2px;text-align:center;clip-path:polygon(0 0,100% 0,100% 100%,0 100%,10px 50%)}
.program__label{margin-left:30px;font-size:14px}
.contacts__entry{font-size:13px;margin-top:24px;line-height:22px}
.album__card{position:absolute;top:2604px;width:260px;height:288px;background:var(--white);padding:10px;box-shadow:0 2px 8px rgba(0,0,0,.1);text-align:center}
.album__photo{width:100%;height:216px}
.album__caption{font-family:"Dancing Script",cursive;font-weight:600;color:var(--green);font-size:19px;margin-top:18px;word-spacing:2px}
.form__field{position:absolute;border-bottom:1.5px solid var(--dash);font-style:italic;font-size:13px;padding-bottom:8px;color:var(--ink)}
.form__rule{position:absolute;left:32px;width:796px;border-bottom:1.5px solid var(--dash)}
.form__send{position:absolute;left:32px;top:355px;width:156px;height:42px;border:1.5px solid var(--ink-soft);background:var(--white);font-family:"Dancing Script",cursive;font-weight:600;font-size:22px;color:var(--ink);text-align:center;line-height:40px}
</style>
</head>
<body>
<div class="foliage foliage--left" role="img" aria-label="Watercolour green leaf vines along the left edge"></div>
<div class="foliage foliage--right" role="img" aria-label="Watercolour green leaf vines along the right edge"></div>
<main class="page"></main>

<div class="rope" style="left:0;top:113px;width:400px"></div>
<div class="rope" style="left:800px;top:113px;width:400px"></div>
<header class="masthead">
  <h1 class="masthead__names">Linda &amp; Daniel</h1>
  <p class="masthead__date">Saturday, 26.05.2018</p>
</header>

<section class="countdown" aria-label="Countdown">
  <div class="countdown__unit"><div class="countdown__value">30</div><div class="countdown__label">DAYS</div></div>
  <div class="countdown__unit"><div class="countdown__value">26</div><div class="countdown__label">HOURS</div></div>
  <div class="countdown__unit"><div class="countdown__value">15</div><div class="countdown__label">MINUTES</div></div>
  <div class="countdown__unit"><div class="countdown__value">27</div><div class="countdown__label">SECONDS</div></div>
</section>

<div class="hero" role="img" aria-label="Photo of a heart drawn in beach sand with the couple's shadows">
  <span class="hero__domain">kolvarenplitz.ch</span>
</div>

<nav class="nav">
  <span>Story</span><i class="nav__dot"></i><span>The Wedding</span><i class="nav__dot"></i><span>Invitation</span><i class="nav__dot"></i><span>Album</span><i class="nav__dot"></i><span>Contact</span>
</nav>

<div class="section-title" style="top:954px"><span>The Story</span></div>
<section class="card story" style="left:168px;top:1142px;width:864px;height:413px">
  <h2 class="script-title story__title">Linda &amp; Daniel</h2>
  <p class="story__text">Lorem ipsum dolor sit amet, consectetur adipiscing elit, sed do eiusmod tempor incididunt ut labore et dolore magna aliqua. Ut enim ad minim veniam, quis nostrud exercitation ullamco laboris nisi ut aliquip ex ea commodo consequat. Duis aute irure dolor in reprehenderit in voluptate velit esse cillum dolore eu fugiat nulla pariatur.</p>
  <p class="story__text" style="margin-top:26px">Sed ut perspiciatis unde omnis iste natus error sit voluptatem accusantium doloremque laudantium, totam rem aperiam, eaque ipsa quae ab illo inventore veritatis et quasi architecto beatae vitae dicta sunt explicabo. Nemo enim ipsam voluptatem quia voluptas sit aspernatur aut odit aut fugit, sed quia consequuntur magni dolores eos qui ratione voluptatem sequi nesciunt. Neque porro quisquam est, qui dolorem ipsum quia dolor sit amet.</p>
</section>
<div class="portrait" style="left:420px;top:1032px;transform:rotate(-5deg)"><div role="img" aria-label="Portrait photo of Daniel" style="background:linear-gradient(160deg,#b7a58c,#6d6f78)"></div></div>
<div class="portrait" style="left:612px;top:1030px;transform:rotate(6deg)"><div role="img" aria-label="Portrait photo of Linda" style="background:linear-gradient(160deg,#d9b27a,#a77f55)"></div></div>

<div class="section-title" style="top:1604px"><span>The Wedding</span></div>
<section class="card venue" style="left:168px;top:1709px;width:418px;height:291px">
  <div class="sprig" style="right:6px;top:6px" role="img" aria-label="Leaf sprig decoration"></div>
  <h2 class="script-title">The Ceremony</h2>
  <div class="venue__item"><svg width="18" height="20" viewBox="0 0 18 20"><path d="M9 0v4M7 2h4M3 10l6-6 6 6v10H3z" fill="none" stroke="#4c4a45" stroke-width="1.6"/></svg><span>St Aldwyn Church</span></div>
  <div class="venue__item"><svg width="18" height="20" viewBox="0 0 18 20"><path d="M9 19C4 12 3 10 3 7a6 6 0 0 1 12 0c0 3-1 5-6 12z" fill="none" stroke="#4c4a45" stroke-width="1.6"/><circle cx="9" cy="7" r="2" fill="#4c4a45"/></svg><span>42 Fernleigh Road, London<span class="venue__link">view map</span></span></div>
  <div class="venue__item"><svg width="18" height="18" viewBox="0 0 18 18"><circle cx="9" cy="9" r="7.5" fill="none" stroke="#4c4a45" stroke-width="1.6"/><path d="M9 4v5l3 2" fill="none" stroke="#4c4a45" stroke-width="1.6"/></svg><span>12:00 PM on 26.05.2018</span></div>
</section>
<section class="card venue" style="left:614px;top:1709px;width:418px;height:291px">
  <div class="sprig" style="right:6px;top:6px" role="img" aria-label="Leaf sprig decoration"></div>
  <h2 class="script-title">The Wedding</h2>
  <div class="venue__item"><svg width="18" height="20" viewBox="0 0 18 20"><path d="M9 0v4M7 2h4M3 10l6-6 6 6v10H3z" fill="none" stroke="#4c4a45" stroke-width="1.6"/></svg><span>Willowmere Hotel</span></div>
  <div class="venue__item"><svg width="18" height="20" viewBox="0 0 18 20"><path d="M9 19C4 12 3 10 3 7a6 6 0 0 1 12 0c0 3-1 5-6 12z" fill="none" stroke="#4c4a45" stroke-width="1.6"/><circle cx="9" cy="7" r="2" fill="#4c4a45"/></svg><span>Ashcombe Gardens London SW9 4LR<span class="venue__link">view map</span></span></div>
  <div class="venue__item"><svg width="18" height="18" viewBox="0 0 18 18"><circle cx="9" cy="9" r="7.5" fill="none" stroke="#4c4a45" stroke-width="1.6"/><path d="M9 4v5l3 2" fill="none" stroke="#4c4a45" stroke-width="1.6"/></svg><span>4:00 PM on 26.05.2018</span></div>
</section>

<section class="card" style="left:168px;top:2035px;width:864px;height:413px">
  <div class="sprig" style="right:8px;top:6px" role="img" aria-label="Leaf sprig decoration"></div>
  <div class="sprig" style="right:8px;bottom:6px;transform:scaleY(-1)" role="img" aria-label="Leaf sprig decoration"></div>
  <div style="position:absolute;left:0;top:0;width:420px;height:100%">
    <h2 class="script-title" style="position:absolute;left:30px;top:36px">The Program</h2>
    <div class="program" style="top:112px">
      <div class="program__row"><span class="program__time">11:30</span><span class="program__label">arriving of the guest</span></div>
      <div class="program__row"><span class="program__time">12:00</span><span class="program__label">start ceremony</span></div>
      <div class="program__row"><span class="program__time">13:30</span><span class="program__label">apero riche</span></div>
      <div class="program__row"><span class="program__time">15:00</span><span class="program__label">fund and games</span></div>
    </div>
  </div>
  <div style="position:absolute;left:478px;top:36px">
    <h2 class="script-title">Family Contact</h2>
    <p class="contacts__entry">Ella Marwood (Linda's Mother)<br>014 268 930</p>
    <p class="contacts__entry">Felix Hartwell (Linda's Father)<br>014 268 930</p>
    <p class="contacts__entry">Nora Castell (Daniel's Mother)<br>014 268 930</p>
    <p class="contacts__entry">Oscar Brenning (Daniel's Father)<br>014 268 930</p>
  </div>
</section>

<div class="section-title" style="top:2500px"><span>Album</span></div>
<figure class="album__card" style="left:173px"><div class="album__photo" role="img" aria-label="Photo of the couple sitting on a wooden jetty" style="background:linear-gradient(160deg,#b8c08a,#8c8f6a)"></div><figcaption class="album__caption">When We First Met</figcaption></figure>
<figure class="album__card" style="left:470px"><div class="album__photo" role="img" aria-label="Photo of the couple embracing" style="background:linear-gradient(160deg,#5b4c45,#2d2a2a)"></div><figcaption class="album__caption">Butterflies in My Stomach</figcaption></figure>
<figure class="album__card" style="left:766px"><div class="album__photo" role="img" aria-label="Photo of the couple dancing outdoors" style="background:linear-gradient(160deg,#c9b089,#9b8468)"></div><figcaption class="album__caption">I Wanna Dance With You</figcaption></figure>

<div class="section-title" style="top:2948px"><span>Contact Us</span></div>
<section class="card" style="left:168px;top:3048px;width:864px;height:444px">
  <div class="sprig" style="left:6px;top:6px;transform:scaleX(-1)" role="img" aria-label="Leaf sprig decoration"></div>
  <div class="sprig" style="right:6px;top:6px" role="img" aria-label="Leaf sprig decoration"></div>
  <h2 class="script-title" style="text-align:center;margin-top:50px;font-size:42px">Send Us Message</h2>
  <div class="form__field" style="left:32px;top:130px;width:380px">First Name</div>
  <div class="form__field" style="left:450px;top:130px;width:378px">Last Name</div>
  <div class="form__field" style="left:32px;top:196px;width:796px">Message</div>
  <div class="form__rule" style="top:260px"></div>
  <div class="form__rule" style="top:306px"></div>
  <div class="form__send">Send</div>
</section>
</body>
</html>
```